Vibrant business card design for Product person in Tech

I'm a 29 y/o female Product manager and I'd like to get a business card designed I can use when networking. I'd love something that stands out. Feel free to experiment with the use of colour, maybe geometrical elements - get creative! I work in the tech industry, so looking for a design without too much of a corporate feel. <br/><br/>The business card should have room for:<br/>Name<br/>Email address<br/>Veltrio

Target Market(s)

Tech

Contact Information for Business Card

Name
Email
Veltrio

Colors
faa54b
00a990
33b8a4
abd037
fbee3f
e667a6
ffcf3e
f59195

```html
<!DOCTYPE html>
<html lang="en">
<head>
<meta charset="utf-8">
<title>Jane Smith – Business Card</title>
<link rel="stylesheet" href="https://fonts.googleapis.com/css2?family=Poppins:wght@400;500;700&display=swap">
<style>
  :root {
    --backdrop: #5c56a0;
    --card-white: #f2f2f2;
    --accent-purple: #5d55a0;
    --accent-yellow: #e9e037;
    --ink: #0d0d0d;
    --graphic-tone: #2e2c3c;
  }
  * { margin: 0; padding: 0; box-sizing: border-box; }
  html, body {
    width: 1200px;
    height: 1000px;
    overflow: hidden;
    background: var(--backdrop);
    font-family: "Poppins", sans-serif;
  }
  .canvas {
    position: relative;
    width: 1200px;
    height: 1000px;
  }
  .card {
    position: absolute;
    top: 226px;
    width: 342px;
    height: 598px;
    border-radius: 18px;
    overflow: hidden;
  }
  .card-front {
    left: 248px;
    background: var(--card-white);
  }
  .card-back {
    left: 647px;
    background: var(--accent-yellow);
  }
  .front-shapes,
  .front-graphic {
    position: absolute;
    left: 0;
    top: 0;
  }
  .identity {
    position: absolute;
    left: 25px;
    top: 22px;
    color: var(--ink);
  }
  .identity-name {
    font-weight: 700;
    font-size: 57px;
    line-height: 50px;
    letter-spacing: 0.6px;
  }
  .identity-role {
    margin-top: 6px;
    margin-left: 5px;
    font-weight: 500;
    font-size: 18.5px;
    line-height: 22px;
  }
  .contact {
    position: absolute;
    right: 30px;
    bottom: 22px;
    text-align: right;
    list-style: none;
    color: var(--ink);
    font-weight: 400;
    font-size: 19px;
    line-height: 23px;
    letter-spacing: 1.2px;
  }
  .back-texture {
    position: absolute;
    inset: 0;
    background:
      linear-gradient(180deg,
        #e6dc45 0%, #d9d056 20%, #e4da48 40%,
        #d8cf58 60%, #e3d949 80%, #dad15a 100%);
  }
  .website {
    position: absolute;
    left: 51px;
    top: 530px;
    width: 237px;
    height: 31px;
    background: var(--accent-purple);
    color: var(--accent-yellow);
    font-weight: 500;
    font-size: 18.5px;
    line-height: 31px;
    text-align: center;
    letter-spacing: 1.1px;
  }
</style>
</head>
<body>
<main class="canvas">
  <section class="card card-front">
    <svg class="front-shapes" width="342" height="598" viewBox="0 0 342 598" aria-hidden="true">
      <circle cx="399" cy="259" r="215" fill="var(--accent-yellow)"/>
      <circle cx="-19" cy="404" r="178" fill="var(--accent-purple)"/>
    </svg>
    <svg class="front-graphic" width="342" height="598" viewBox="0 0 342 598" role="img" aria-label="Diagonal band of black horizontal stripes crossing both circles">
      <polygon points="282,204 314,261 54,396 26,341" fill="var(--graphic-tone)"/>
    </svg>
    <header class="identity">
      <h1 class="identity-name">Jane<br>Smith</h1>
      <p class="identity-role">Product manager</p>
    </header>
    <ul class="contact">
      <li class="contact-phone">012 345 645</li>
      <li class="contact-email">EMAIL@DOMAIN.COM</li>
      <li class="contact-profile">VELTRIO/USERNAME</li>
    </ul>
  </section>

  <section class="card card-back">
    <div class="back-texture" role="img" aria-label="Yellow field with a glitchy pattern of thin horizontal purple lines"></div>
    <p class="website">WWW.WEBSITE.COM</p>
  </section>
</main>
</body>
</html>
```